Flyer for handout on the street to attract people

Create two different leaflets for handing out to recruit volunteers to participate in a program of biological specimen donation. The leaflet should be catchy, have some graphics, and have enough info that people will want to sign up by going to the website for more information.

Leave room on each leaflet for some English and Chinese. The example of Leaflet #1 will need approximately the same space in order to have the Chinese translation.

The example of Leaflet #2 already has a Chinese translation which can be incorporated.

The size should be half of A4 page. If it is a whole A4 page it may also be considered.

Leaflet #1 Text:

RECRUITING HEALTHY VOLUNTEERS (and get PAID)!

The Orient Flora Vault is recruiting healthy individuals in Hong Kong to participate in a scientific research project to study bacteria in healthy guts. They will pay you $200 HKD per day to participate in the study. If you qualify, you can earn up to $4800 a month!

Incidences of digestive and colon diseases are increasing rapidly in Hong Kong, and part of the key to solving this problem is understanding gut bacteria. There are up to 100 trillion bacteria and microbes in every human gut, including yours. Scientists have recently uncovered that these bacteria are key human digestion and immune systems. However, when your gut bacteria are imbalanced, it can cause all kinds of problems such as indigestion, IBS, ulcerative colitis, or clostridium difficile infection.

Every year, more than 500,000 people are infected by a toxic bacteria called clostridium difficile, which causes severe stomach pain, and sometimes even death. YOUR GUT BACTERIA COULD BE KEY TO HELPING THESE SICK PATIENTS.

CRITERIA FOR PARTICIPATING: If you are a healthy adult between 18-50 years old; no digestive problems and no recent medications, then the Orient LifeVault needs your participation! They will pay you $200 HKD per day to participate in the study. If you qualify, you can earn up to $4800 a month! To learn more information, go to http://www.orientlifevault.example or send a whatsapp to 6372 8415

Leaflet #2 Text:

Get paid to give your poopoo!

Literally.

Asia’s first commercial stool bank is recruiting donors. Get paid up to $4,800 HKD per month for your poop donations at our convenient Central Hong Kong lab.

Answer the questionnaire to see if you qualify at www.orientlifevault.example or call 6372 8415 for more information.

你好屎!

我地就係想要你D好屎。

全亞洲第一間商業糞便銀行正招募捐贈者。請即前往我們位於中環的糞便銀行成為捐贈者,每月最多可賺取6,000港元的酬勞。

想知道自己是否適合捐贈?馬上點擊 www.orientlifevault.example/donate 回答問題或撥打0000-0000查詢詳情。

Target Market(s)

Young professionals, middle-class

Industry/Entity Type

Medical

Font styles to use
Serif
Sans Serif
Decorative

Requirements
Must have
• The text. Two leaflet examples. Some graphics.
Nice to have
• Catchy design. Something people will see while walking past and go ahead and take it from someone handing out flyers.
Should not have
• Only text. Should be colorful and have graphics. (Can download or shutterstock photos.)

```html
<!DOCTYPE html>
<html lang="en">
<head>
<meta charset="utf-8">
<title>Orient Flora Vault – Recruiting Healthy Volunteers</title>
<link rel="stylesheet" href="https://fonts.googleapis.com/css2?family=Lato:ital,wght@0,400;0,700;0,900;1,700;1,900&family=Libre+Baskerville:wght@700&family=Oswald:wght@500;700&display=swap">
<style>
:root{
  --blue:#1f6fe0;
  --royal:#1436c8;
  --navy:#0a12a6;
  --ink:#1d1d24;
  --grey:#c9cbd3;
  --paper:#ffffff;
  --stage:#ececec;
  --aqua:#35e3e0;
}
*{box-sizing:border-box;margin:0;padding:0}
html,body{width:1142px;height:1200px;overflow:hidden;background:var(--stage)}
.flyer{position:absolute;left:161px;top:20px;width:820px;height:1160px;background:var(--paper);overflow:hidden;font-family:"Lato",sans-serif;color:var(--ink)}
.abs{position:absolute}
.top-band{left:0;top:0;width:100%;height:12px;background:var(--blue)}
.bottom-band{left:0;bottom:0;width:100%;height:70px;background:var(--navy)}
.decor{left:0;top:0}
.brand{display:flex;align-items:center;gap:10px;font-family:"Lato",sans-serif;font-weight:700;font-size:19px;color:var(--royal);white-space:nowrap}
.brand-dot{width:26px;height:26px;border-radius:50%;background:var(--royal)}
.brand-top{left:52px;top:52px}
.brand-mid{left:628px;top:698px}
.headline{left:52px;top:140px;font-weight:900;font-size:64px;letter-spacing:1px;color:var(--blue);line-height:1}
.subhead{left:56px;top:210px;font-family:"Libre Baskerville",serif;font-weight:700;font-size:30px;letter-spacing:1px;color:var(--ink)}
.body{left:56px;top:264px;width:400px;font-size:10.5px;line-height:1.42}
.body p{margin-bottom:7px}
.body .key{color:var(--royal);font-weight:700;font-size:10.5px;text-transform:uppercase}
.badge{z-index:3;display:flex;flex-direction:column;align-items:center;justify-content:center;text-align:center;border-radius:50%;background:var(--paper);border:7px solid var(--royal);box-shadow:0 0 0 4px var(--aqua) inset}
.badge-day{left:466px;top:244px;width:140px;height:140px;font-family:"Oswald",sans-serif;font-weight:700;font-size:15px;line-height:1.15;padding:8px}
.badge-day .accent{color:var(--blue);font-weight:500;font-size:14px}
.criteria{z-index:2;left:476px;top:360px;width:330px;height:182px;background:var(--blue);border-radius:6px 0 0 6px;color:#fff;padding:14px 22px 10px 26px}
.criteria h2{font-family:"Lato",sans-serif;font-weight:900;font-size:20px;text-align:center;line-height:1}
.criteria h3{font-size:13px;font-weight:700;letter-spacing:1px;text-align:center;margin:4px 0 8px;background:var(--paper);color:var(--royal);padding:2px 0;border-radius:3px}
.criteria ul{list-style:none;font-size:14px;line-height:1.32;text-align:right}
.criteria li::after{content:"";display:inline-block;width:9px;height:9px;border-radius:50%;background:#fff;margin-left:8px;vertical-align:middle}
.criteria li.plain::after{display:none}
.qualify-strip{left:446px;top:542px;width:360px;height:24px;background:#0b0b12;color:var(--aqua);font-size:13px;font-style:italic;font-weight:700;padding:4px 12px;text-align:right;white-space:nowrap}
.learn{left:420px;top:572px;width:386px;font-size:11px;text-align:right;line-height:1.45}
.learn a{color:var(--royal);font-weight:700;text-decoration:none}
.stool-head{left:50px;top:600px;font-weight:900;font-style:italic;font-size:28px;line-height:1.2;text-transform:uppercase;color:var(--blue);letter-spacing:1.5px}
.photo{display:block}
.photo-team{left:470px;top:12px}
.photo-host{left:26px;top:742px;width:140px;height:220px;border-radius:10px;background:linear-gradient(160deg,#f4f6fb,#d9e2f3)}
.callout{z-index:1;left:262px;top:730px;width:330px;height:90px;border:2px solid #555;border-radius:18px;background:var(--paper);box-shadow:4px 6px 10px rgba(0,0,0,.18);padding:16px 20px;font-size:18px;line-height:1.3}
.cta{left:176px;top:862px;width:424px;height:160px;background:var(--blue);border-radius:18px;color:#fff;padding:24px 26px;font-size:16px;line-height:1.4}
.cta .call{display:inline-block;margin-top:10px;border:2px solid #fff;border-radius:20px;padding:2px 14px}
.badge-pay{left:614px;top:792px;width:172px;height:172px;font-family:"Lato",sans-serif;font-size:19px;line-height:1.12;font-weight:700}
.badge-pay .big{color:var(--blue);font-family:"Oswald",sans-serif;font-size:24px}
.badge-pay .amt{color:var(--royal);font-weight:900;font-size:21px}
</style>
</head>
<body>
<main class="flyer">
  <div class="abs top-band"></div>

  <svg class="abs decor" width="820" height="1160" viewBox="0 0 820 1160" aria-hidden="true">
    <path d="M0 96 Q220 100 470 124 L470 136 Q220 112 0 114 Z" fill="var(--royal)"/>
    <path d="M120 116 Q300 120 470 140 L470 145 Q300 128 120 124 Z" fill="var(--grey)"/>
    <path d="M0 506 Q250 508 460 548 L460 562 Q250 524 0 524 Z" fill="var(--royal)"/>
    <path d="M0 530 Q200 534 380 568 L380 575 Q200 542 0 538 Z" fill="var(--grey)"/>
    <path d="M820 640 Q600 630 586 760 Q600 868 820 880" fill="none" stroke="var(--royal)" stroke-width="5"/>
    <path d="M820 658 Q625 650 610 740" fill="none" stroke="var(--grey)" stroke-width="10"/>
  </svg>

  <div class="abs brand brand-top"><span class="brand-dot"></span>Orient Flora Vault</div>

  <svg class="abs photo photo-team" width="350" height="300" viewBox="0 0 350 300" role="img" aria-label="Photo of five smiling doctors in white coats giving a thumbs up">
    <defs><linearGradient id="team" x1="0" y1="0" x2="1" y2="1"><stop offset="0" stop-color="#f3f5fa"/><stop offset="1" stop-color="#d3dcec"/></linearGradient></defs>
    <path d="M70 0 H350 V300 Q160 270 70 120 Q40 60 70 0 Z" fill="url(#team)"/>
    <path d="M70 0 Q40 60 70 120 Q160 270 350 300" fill="none" stroke="var(--royal)" stroke-width="8"/>
  </svg>

  <h1 class="abs headline">RECRUITING</h1>
  <p class="abs subhead">HEALTHY VOLUNTEERS</p>

  <div class="abs body">
    <p>The Orient Flora Vault is recruiting healthy individuals in Hong Kong to participate in a scientific research project to study bacteria in healthy guts. They will pay you $200 HKD per day to participate in the study. If you qualify, you can earn up to $4800 a month!</p>
    <p>Incidences of digestive and colon diseases are increasing rapidly in Hong Kong, and part of the key to solving this problem is understanding gut bacteria. There are up to 100 trillion bacteria and microbes in every human gut, including yours. Scientists have recently uncovered that these bacteria are key human digestion and immune systems. However, when your gut bacteria are imbalanced, it can cause all kinds of problems such as indigestion, IBS, ulcerative colitis, or clostridium difficile infection.</p>
    <p>Every year, more than 500,000 people are infected by a toxic bacteria called clostridium difficile, which causes severe stomach pain, and sometimes even death.</p>
    <p class="key">Your gut bacteria could be key to helping these sick patients.</p>
  </div>

  <div class="abs badge badge-day">$200 HKD<br>per day<span class="accent">to participate<br>in the study</span></div>

  <section class="abs criteria">
    <h2>CRITERIA</h2>
    <h3>FOR PARTICIPATING:</h3>
    <ul>
      <li>If you are a healthy adult<br>between 18-50 years old</li>
      <li>no digestive problems</li>
      <li>no recent medications</li>
      <li class="plain">Then the Orient LifeVault needs<br>your participation!</li>
    </ul>
  </section>
  <div class="abs qualify-strip">If you qualify, you can earn up to $4800/month!</div>
  <p class="abs learn">To learn more information: go to <a href="http://www.orientlifevault.example">http://www.orientlifevault.example</a><br>or send a whatsapp to 6372 8415</p>

  <h2 class="abs stool-head">Asia's first<br>commercial stool bank<br>is recruiting donors.</h2>

  <div class="abs brand brand-mid"><span class="brand-dot"></span>Orient Flora Vault</div>

  <div class="abs photo photo-host" role="img" aria-label="Photo of a smiling nurse in a white uniform presenting with an open hand"></div>

  <p class="abs callout">For your poop donations at our convenient Central Hong Kong lab.</p>

  <div class="abs cta">Answer the questionnaire to see if you qualify at<br>www.orientlifevault.example<br><span class="call">or call 6372 8415 for more information.</span></div>

  <div class="abs badge badge-pay">Get<span class="big">paid up to</span><span class="amt">$4,800 HKD</span>per month</div>

  <div class="abs bottom-band"></div>
</main>
</body>
</html>
```